Construction Website Design for presskit

Update:
I like this theme as a starting point. It seems like a very good start. Fonts, colors, motion, etc. https://advisory.kelbrowthemes.com/
***************************************************************************************

I want a new website design that can be implemented in presskit. Here is my existing site: www.vantornmeasures.com
Attached is a document with the copy, requirements, sample images, etc. Let me know what questions you have.

Here is a sample of the info, but review the attached document for everything:

Website layout:
Title Bar
• Home
• Expertise
• Takeoffs
• Divisions Serviced (redesign from orig page: (http://www.vantornmeasures.com/scope-list/)
• Member Login
Requirements
• Home page has a slider with 3 dimmed commercial construction images and copy overlay
• Request for Proposal Form should be over the slider and the same look and location on every page.
• “Request For Proposal” – No Obligation
o Company Name
o Contact Name
o Contact Phone
o Contact Email
• Use the copy below for the pages
• Split the Client Testimonials among the pages

Target Market(s)

B2B - Construction Companies

Industry/Entity Type

Construction

Number of Pages Required

4 page

Font styles to use
Serif

Colors
0255a3
3276b5
85abd2
d0dfed

Requirements
Must have
• Construction images in slider
• Request for proposal form
• testimonials

```html
<!DOCTYPE html>
<html lang="en">
<head>
<meta charset="utf-8">
<title>Vantorn Measures – Construction Takeoff Experts</title>
<link href="https://fonts.googleapis.com/css2?family=Montserrat:wght@300;400;500;600;700&display=swap" rel="stylesheet">
<style>
:root{
  --navy:#22408a;
  --navy-deep:#1b3372;
  --sky:#1d9bd7;
  --ice:#e2f3f8;
  --topbar:#e6f5f9;
  --teal-blue:#1c5a8c;
  --ink:#3a3a3a;
  --grey:#7a7a7a;
  --light-grey:#9a9a9a;
  --footer:#3b3b3b;
  --footer-base:#2f2f2f;
  --white:#ffffff;
}
*{margin:0;padding:0;box-sizing:border-box}
html,body{width:1200px;height:2476px;overflow:hidden}
body{font-family:'Montserrat',sans-serif;color:var(--ink);background:var(--white);position:relative}
.abs{position:absolute}

/* top bar */
.topbar{top:0;left:0;width:1200px;height:25px;background:var(--topbar)}
.topbar-links{right:72px;top:5px;font-size:11px;color:var(--navy);display:flex;gap:22px}
.topbar-links span{display:flex;align-items:center;gap:6px}

/* header */
.header{top:25px;left:0;width:1200px;height:87px;background:var(--white)}
.brand{left:58px;top:16px;color:var(--navy)}
.brand-name{font-size:30px;font-weight:500;letter-spacing:.5px;line-height:32px;display:flex;align-items:center;gap:10px}
.brand-name i{width:12px;height:12px;background:var(--sky);display:inline-block}
.brand-tag{font-size:14px;font-weight:500;letter-spacing:.6px;margin-left:22px;margin-top:2px}
.contact-item{top:26px;display:flex;gap:14px;font-size:13px;line-height:26px;color:var(--ink)}
.contact-item .blue{color:var(--navy)}

/* nav */
.nav{top:112px;left:0;width:1200px;height:75px;background:var(--navy)}
.nav-items{left:66px;top:28px;display:flex;font-size:14px;color:var(--white)}
.nav-items .item{display:flex;align-items:center}
.nav-items .sep{margin:0 22px;color:#7f93c4}
.nav-items .active{color:var(--sky)}
.caret{margin-left:8px}

/* hero */
.hero{top:187px;left:0;width:1200px;height:597px;background:linear-gradient(100deg,#30435f 0%,#4f6b8c 30%,#6e86a3 45%,#3e5574 60%,#2b3a52 100%)}
.hero-shade{top:187px;left:825px;width:375px;height:597px;background:rgba(15,22,34,.55)}
.hero-title{left:46px;top:410px;font-size:68px;font-weight:700;color:var(--white);letter-spacing:1px}
.hero-title span{color:var(--sky)}
.hero-rule{left:50px;top:492px;width:500px;height:1px;background:rgba(255,255,255,.4)}
.hero-sub{left:46px;top:506px;font-size:14px;color:var(--white)}
.btn-outline{left:50px;top:574px;width:132px;height:36px;border:2px solid var(--white);color:var(--white);font-size:12px;display:flex;align-items:center;justify-content:center;gap:12px}

.rfp-title{left:858px;top:268px;width:296px;height:40px;color:var(--sky);font-size:19px;font-weight:600;display:flex;align-items:center;justify-content:center}
.rfp-text{left:860px;top:344px;width:292px;text-align:center;font-size:12px;line-height:21px;color:var(--white)}
.field{left:842px;width:318px;height:36px;background:var(--white);font-size:12px;color:#333;padding-left:16px;display:flex;align-items:center;border-left:3px solid var(--sky)}
.submit{left:842px;top:632px;width:318px;height:34px;background:var(--sky);color:var(--white);font-size:12px;font-weight:600;display:flex;align-items:center;justify-content:center;border:1px solid var(--white)}

/* intro */
.section-title{left:0;width:1200px;text-align:center;color:var(--navy);font-size:36px}
.section-title b{font-weight:700}
.section-title span{font-weight:300}
.intro-sub{top:932px;left:0;width:1200px;text-align:center;font-size:16px;color:var(--ink)}
.intro-text{top:984px;left:100px;width:1000px;text-align:center;font-size:12.5px;line-height:26px;color:var(--grey);font-weight:300}
.feature-icon{width:80px;height:80px;border-radius:50%;background:var(--navy);display:flex;align-items:center;justify-content:center}
.feature-title{font-size:21px;color:var(--navy)}
.feature-text{font-size:12.5px;line-height:23.5px;color:var(--grey);text-align:justify}

/* cutting edge */
.band{top:1370px;left:0;width:1200px;height:220px;background:var(--ice)}
.band-title{left:66px;top:1428px;font-size:36px;color:var(--navy-deep)}
.band-title span{font-weight:300;color:#555}
.band-title b{font-weight:700}
.band-text{left:66px;top:1476px;width:800px;font-size:17px;line-height:27px;color:#a9b3b8;font-weight:300;letter-spacing:.3px}
.btn-frame{left:886px;top:1464px;width:164px;height:49px;border:2px solid var(--navy);color:var(--navy);font-size:14px;font-weight:500;display:flex;align-items:center;justify-content:center;gap:12px}

/* testimonials */
.clients{top:1658px;left:0;width:1200px;height:537px;background:linear-gradient(180deg,#1d5c8f 0%,#1a5585 60%,#174d7a 100%)}
.clients-title{top:1705px;left:0;width:1200px;text-align:center;color:var(--white);font-size:36px}
.clients-title b{font-weight:700}.clients-title span{font-weight:300}
.clients-sub{top:1766px;left:0;width:1200px;text-align:center;font-size:15px;color:var(--white);font-weight:500}
.quote-mark{font-size:70px;font-weight:700;color:var(--white);line-height:1}
.quote{font-size:13.5px;line-height:27px;color:var(--white);text-align:justify}
.avatar{width:70px;height:70px;border-radius:50%;background:linear-gradient(160deg,#c9a58a,#6d4b3a);border:3px solid var(--white)}
.person{color:var(--white);font-size:13px}
.person b{font-weight:700;display:block;margin-bottom:8px}
.person i{font-size:12px}

/* footer */
.footer{top:2203px;left:0;width:1200px;height:223px;background:var(--footer)}
.footer-base{top:2426px;left:0;width:1200px;height:50px;background:var(--footer-base);color:#cfcfcf;font-size:11px;display:flex;align-items:center;justify-content:center}
.f-brand{left:92px;top:2240px;color:var(--white)}
.f-brand .n{font-size:24px;font-weight:500;letter-spacing:.5px}
.f-brand .t{font-size:12px;letter-spacing:.6px;margin-top:2px}
.f-line{font-size:12px;color:#d6d6d6;line-height:22px}
.f-head{font-size:14px;color:var(--white);font-weight:500;letter-spacing:.3px}
.f-list{font-size:12px;color:#cfcfcf;line-height:26.5px;list-style:none}
.f-list li::before{content:"·";margin-right:12px}
.social{left:957px;top:2284px;width:166px;height:46px;border:2px solid #dfdfdf;background:#4a4a4a;color:var(--white);font-size:22px;font-weight:600;display:flex;align-items:center;justify-content:center}
.cards{left:957px;top:2384px;display:flex;gap:5px}
.cards span{width:39px;height:22px;background:var(--white);font-size:8.5px;font-weight:600;color:var(--navy);display:flex;align-items:center;justify-content:center}
</style>
</head>
<body>

<div class="abs topbar"></div>
<div class="abs topbar-links">
  <span><svg width="11" height="11" viewBox="0 0 12 12"><path d="M1 1h5v2H3v6h3v2H1z M6 4l3 2-3 2z" fill="#22408a"/></svg>Signup</span>
  <span><svg width="8" height="12" viewBox="0 0 8 12"><rect x="1" y="0.5" width="6" height="11" rx="1" fill="none" stroke="#22408a"/></svg>Contact</span>
</div>

<header class="abs header">
  <div class="abs brand">
    <div class="brand-name"><i></i>VANTORN MEASURES</div>
    <div class="brand-tag">CONSTRUCTION TAKEOFF EXPERTS</div>
  </div>
  <div class="abs contact-item" style="left:745px">
    <svg width="34" height="34" viewBox="0 0 34 34"><rect x="6" y="3" width="15" height="27" rx="2" fill="none" stroke="#22408a" stroke-width="2.5"/><line x1="11" y1="25" x2="16" y2="25" stroke="#22408a" stroke-width="2"/><path d="M25 12a6 6 0 0 1 0 9M28 9a10 10 0 0 1 0 15" fill="none" stroke="#22408a" stroke-width="2"/></svg>
    <div><div>(555) 014-2390</div><div class="blue">hello@vantornmail.com</div></div>
  </div>
  <div class="abs contact-item" style="left:952px">
    <svg width="32" height="32" viewBox="0 0 32 32"><circle cx="16" cy="16" r="13" fill="none" stroke="#22408a" stroke-width="2.5"/><path d="M16 8v8l5 4" fill="none" stroke="#22408a" stroke-width="2.5"/></svg>
    <div><div>9 am to 8 pm</div><div>Monday - Saturday</div></div>
  </div>
</header>

<nav class="abs nav">
  <div class="abs nav-items">
    <span class="item active">Home</span><span class="sep">|</span>
    <span class="item">Expertise<svg class="caret" width="8" height="6" viewBox="0 0 8 6"><path d="M1 1l3 3 3-3" stroke="#fff" fill="none" stroke-width="1.4"/></svg></span><span class="sep">|</span>
    <span class="item">Takeoffs<svg class="caret" width="8" height="6" viewBox="0 0 8 6"><path d="M1 1l3 3 3-3" stroke="#fff" fill="none" stroke-width="1.4"/></svg></span><span class="sep">|</span>
    <span class="item">Divisions Serviced<svg class="caret" width="8" height="6" viewBox="0 0 8 6"><path d="M1 1l3 3 3-3" stroke="#fff" fill="none" stroke-width="1.4"/></svg></span><span class="sep">|</span>
    <span class="item">Members Login</span>
  </div>
  <svg class="abs" style="left:1074px;top:31px" width="14" height="14" viewBox="0 0 14 14"><circle cx="6" cy="6" r="4" fill="none" stroke="#fff" stroke-width="2"/><path d="M9 9l4 4" stroke="#fff" stroke-width="2"/></svg>
</nav>

<section class="abs hero" role="img" aria-label="Dimmed photo of a glass commercial tower under construction with a crane, set over blueprints"></section>
<div class="abs hero-shade"></div>
<h1 class="abs hero-title">C<span>O</span>NFIDENCE</h1>
<div class="abs hero-rule"></div>
<p class="abs hero-sub">Accurate and reliable, we help you propose on more work without risk.</p>
<div class="abs btn-outline">Read More <svg width="7" height="10" viewBox="0 0 7 10"><path d="M1 1l4 4-4 4" stroke="#fff" fill="none" stroke-width="1.6"/></svg></div>

<svg class="abs" style="left:858px;top:266px" width="296" height="44" viewBox="0 0 296 44"><path d="M1 14V1h13M282 1h13v13M295 30v13h-13M14 43H1V30" fill="none" stroke="#1d9bd7" stroke-width="1.5"/></svg>
<h2 class="abs rfp-title">REQUEST FOR PROPOSAL</h2>
<p class="abs rfp-text">Lorem Ipsum is simply dummy text of the printing and typesetting industry.</p>
<div class="abs field" style="top:408px">COMPANY NAME</div>
<div class="abs field" style="top:463px">CONTACT NAME</div>
<div class="abs field" style="top:518px">PHONE</div>
<div class="abs field" style="top:572px">EMAIL ADDRESS</div>
<div class="abs submit">SUBMIT</div>

<h2 class="abs section-title" style="top:870px"><b>VANTORN</b> <span>MEASURES</span></h2>
<p class="abs intro-sub">We cover a rage of industries as diverse as you expected...</p>
<p class="abs intro-text">Dedicated to saving our clients time and money by specializing in accurate, reliable materials quantity calculations, Vantorn Measures allows general contractors to confidently propose on more work with less stress. To receive a no-obligation answer to your takeoff needs complete the Request for Proposal form. Vantorn Measures will provide a comprehensive proposal detailing the hours required and payment options that are easily refined to both near- and long-term needs.</p>

<div class="abs feature-icon" style="left:51px;top:1115px">
  <svg width="44" height="44" viewBox="0 0 44 44"><circle cx="22" cy="22" r="14" fill="none" stroke="#fff" stroke-width="2.5"/><circle cx="22" cy="8" r="5" fill="#22408a" stroke="#fff" stroke-width="2.5"/><circle cx="10" cy="29" r="5" fill="#22408a" stroke="#fff" stroke-width="2.5"/><circle cx="34" cy="29" r="5" fill="#22408a" stroke="#fff" stroke-width="2.5"/></svg>
</div>
<h3 class="abs feature-title" style="left:158px;top:1110px">Process</h3>
<p class="abs feature-text" style="left:155px;top:1140px;width:406px">Once the proposal is approved, clients fund their account and allocate their hours as desired - project-by-project, monthly, as-needed, or otherwise. Our service and products are completely tailored to each client based on the fundamental factors that make your business distinct from all others.</p>

<div class="abs feature-icon" style="left:622px;top:1115px">
  <svg width="40" height="40" viewBox="0 0 40 40"><path d="M6 6v28h28" fill="none" stroke="#fff" stroke-width="2.5"/><path d="M12 27l7-8 5 5 9-11" fill="none" stroke="#fff" stroke-width="2.5"/><path d="M27 13h6v6" fill="none" stroke="#fff" stroke-width="2.5"/></svg>
</div>
<h3 class="abs feature-title" style="left:726px;top:1110px">Benefits</h3>
<p class="abs feature-text" style="left:726px;top:1140px;width:374px">Accurate, reliable quantities delivered as-scheduled and expected allow your key staff to invest their time in quality, safety, profit, and client relationships. An extra set of hands in your bid room helps you put out more proposals and takes a tedious task off your to-do list whenever you need it without the obligation of a full-time salary.</p>

<section class="abs band"></section>
<h2 class="abs band-title"><span>The</span> <b>Cutting Edge of Business</b></h2>
<p class="abs band-text">Unlike other Frameworks which try to cover everything, it has been built specifically for presskit. Aliquam sapien est, mollis id mattis id, scelerisque sed dolor.</p>
<svg class="abs" style="left:878px;top:1455px" width="180" height="67" viewBox="0 0 180 67"><path d="M166 1h13v13M1 53v13h13" fill="none" stroke="#22408a" stroke-width="2"/></svg>
<div class="abs btn-frame">Read More <svg width="10" height="10" viewBox="0 0 10 10"><path d="M0 5h8M5 2l3 3-3 3" stroke="#22408a" fill="none" stroke-width="1.6"/></svg></div>

<section class="abs clients" role="img" aria-label="Dim blue-toned photo of a construction site with cranes"></section>
<h2 class="abs clients-title"><b>CLIENTS</b> <span>REMARK</span></h2>
<p class="abs clients-sub">The best of the best is here...</p>

<div class="abs quote-mark" style="left:108px;top:1868px">&#8221;</div>
<p class="abs quote" style="left:173px;top:1868px;width:393px">Vantorn Measures does outstanding work, accurate, detailed, and reliable. The consultant on my account knows what I want in the breakdown and produces the information exactly as I need it.Time, money and confidence, Vantorn Measures hits the mark every time.”</p>
<div class="abs avatar" role="img" aria-label="Client portrait" style="left:109px;top:2031px"></div>
<div class="abs person" style="left:195px;top:2044px"><b>Dana Whitfield, President</b><i>- Ridgeline Roofing</i></div>

<div class="abs quote-mark" style="left:644px;top:1868px">&#8221;</div>
<p class="abs quote" style="left:708px;top:1868px;width:394px">We get an influx of great opportunities and sometimes it's more than we can handle. Vantorn Measures fills the gap and helped us to grow our business. It's really excellent to have a genuine, always-ready ally in our estimating efforts.</p>
<div class="abs avatar" role="img" aria-label="Client portrait" style="left:652px;top:2031px"></div>
<div class="abs person" style="left:738px;top:2044px"><b>Arjun Mehra</b><i>- Harborview Builders, LLC.</i></div>

<footer class="abs footer"></footer>
<div class="abs f-brand"><div class="n">VANTORN MEASURES</div><div class="t">CONSTRUCTION TAKEOFF EXPERTS</div></div>
<svg class="abs" style="left:104px;top:2324px" width="14" height="18" viewBox="0 0 14 18"><path d="M7 17s6-6.5 6-10.5A6 6 0 0 0 1 6.5C1 10.5 7 17 7 17z" fill="#fff"/><circle cx="7" cy="6.5" r="2.2" fill="#3b3b3b"/></svg>
<div class="abs f-line" style="left:135px;top:2320px">Vantorn Measures, Po Box-218,<br>Fairmont, GA 30112</div>
<svg class="abs" style="left:104px;top:2371px" width="14" height="14" viewBox="0 0 14 14"><path d="M3 1l3 3-2 2c1 2 2 3 4 4l2-2 3 3-2 2C6 13 1 8 1 3z" fill="#fff"/></svg>
<div class="abs f-line" style="left:138px;top:2366px">(555) 014-2390</div>

<h4 class="abs f-head" style="left:485px;top:2249px">QUICK LINKS</h4>
<ul class="abs f-list" style="left:485px;top:2292px"><li>Expertise</li><li>Takeoffs</li><li>Divisions Serviced</li></ul>
<h4 class="abs f-head" style="left:698px;top:2249px">CUSTOMER INFO</h4>
<ul class="abs f-list" style="left:707px;top:2292px"><li>Customer Signup</li><li>Privacy Policy</li><li>Contact</li></ul>
<h4 class="abs f-head" style="left:957px;top:2249px">FOLLOW US @</h4>
<div class="abs social">Linkwork</div>
<h4 class="abs f-head" style="left:957px;top:2359px">WE PROUDLY ACCEPT:</h4>
<div class="abs cards"><span>Cardia</span><span>Paywell</span><span>Orbcard</span><span>Expo</span></div>
<div class="abs footer-base">Copyright © 2019 Vantorn Measures, All rights reserved.</div>

</body>
</html>
```